Letterhead for new real estate company in South Africa named Lofthaven

A letterhead with the directors and company details to be editable as these changes often

Target Market(s)

In line with our logo brief and our newly designed logo and corporate fee

Industry/Entity Type

Real Estate

Requirements
Must have
• Details as per the sample letterhead provided.

```html
<!DOCTYPE html>
<html lang="en">
<head>
<meta charset="utf-8">
<title>Lofthaven Letterhead</title>
<link rel="stylesheet" href="https://fonts.googleapis.com/css2?family=Inter:wght@400;500;700&display=swap">
<style>
  :root {
    --brand-green: #36b06f;
    --brand-brown: #6e6558;
    --accent-red: #d8262e;
    --ink: #1b1b1b;
    --mint-faint: #dcefe4;
    --paper: #ffffff;
  }
  * { margin: 0; padding: 0; box-sizing: border-box; }
  html, body { width: 927px; height: 1200px; overflow: hidden; background: var(--paper); }
  body { font-family: "Inter", Arial, sans-serif; color: var(--ink); }

  .letterhead { position: relative; width: 927px; height: 1200px; overflow: hidden; background: var(--paper); }

  .edge-bars { position: absolute; left: 0; top: 0; width: 14px; height: 1200px; }

  .watermark {
    position: absolute; left: 330px; top: 560px; width: 540px; height: 540px;
    border-radius: 50%; background: var(--mint-faint); opacity: 0.55;
  }

  .brand { position: absolute; left: 46px; top: 52px; display: flex; align-items: center; gap: 16px; }
  .brand-dot { width: 46px; height: 46px; border-radius: 50%; background: var(--brand-green); }
  .brand-name { font-size: 50px; font-weight: 500; color: var(--brand-green); letter-spacing: -1px; line-height: 1; }

  .directors { position: absolute; right: 28px; top: 38px; text-align: right; font-size: 13px; line-height: 17px; }
  .directors-title { color: var(--accent-red); font-weight: 700; margin-bottom: 6px; }
  .directors-name { font-weight: 700; }
  .franchise-note { margin-top: 20px; font-weight: 400; }

  .footer-rule { position: absolute; left: 13px; right: 0; top: 1077px; height: 1px; background: var(--brand-green); }

  .company-details {
    position: absolute; left: 14px; right: 0; top: 1094px; text-align: center;
    font-size: 14.5px; line-height: 18px;
  }
  .company-details .contact { margin-top: 7px; }
  .company-details .web { margin-top: 7px; }
</style>
</head>
<body>
<main class="letterhead">
  <svg class="edge-bars" viewBox="0 0 14 1200" aria-hidden="true">
    <rect x="0" y="0" width="9" height="1200" fill="var(--brand-brown)"/>
    <polygon points="9,0 14,0 14,1112 9,1118" fill="var(--brand-green)"/>
  </svg>

  <div class="watermark" aria-hidden="true"></div>

  <header class="brand">
    <span class="brand-dot" aria-hidden="true"></span>
    <span class="brand-name">Lofthaven</span>
  </header>

  <aside class="directors">
    <p class="directors-title">Directors:</p>
    <p class="directors-name">R Vandermeer</p>
    <p class="directors-name">KL Ashford-Brink</p>
    <p class="franchise-note">Each franchise is independently owned and operated</p>
  </aside>

  <div class="footer-rule"></div>

  <footer class="company-details">
    <p>Highveld Estates (Pty) Ltd Va Homestead Realty Sandton/Fourways, Reg No: 2019/458207/07</p>
    <p>Shop GF12B, Oakridge Square, Corner Elm Avenue &amp; Kestrel Road Oakridge, South Africa</p>
    <p class="contact">Tel: 010 555 0142</p>
    <p class="web">Web: www homesteadrealty.co.za</p>
  </footer>
</main>
</body>
</html>
```